Kestrel Plumbing Solutions

This is for my new plumbing company, I have attached an example of what I’m going for but want it to look better.

Target Market(s)

Home owners, real estate, etc.

Industry/Entity Type

Plumbing

• As per my logo and other examples uploaded

Colors

Designer to choose colors to be used in the design.

Requirements
Must have
• Must include my logo provided and similar to my flyer I have attached but better

```html
<!DOCTYPE html>
<html lang="en">
<head>
<meta charset="utf-8">
<title>Kestrel Plumbing Solutions – Flyer</title>
<link rel="stylesheet" href="https://fonts.googleapis.com/css2?family=Bebas+Neue&family=Oswald:wght@300;500&family=Poppins:wght@600;700;800&display=swap">
<style>
  :root{
    --ink:#3a3a3c;
    --charcoal:#2f2f31;
    --blue:#3d94e6;
    --lime:#b8ea4c;
    --white:#ffffff;
  }
  *{margin:0;padding:0;box-sizing:border-box}
  html,body{width:900px;height:1200px;overflow:hidden;background:var(--white)}
  .flyer{position:relative;width:900px;height:1200px;overflow:hidden;background:var(--white);font-family:"Poppins",sans-serif}
  .top-band{position:absolute;left:0;top:0;width:900px;height:325px;background:var(--charcoal)}
  .tools-photo{position:absolute;left:450px;top:0;width:450px;height:325px;
    background:linear-gradient(135deg,#3a3a3c 0%,#8d8d90 35%,#e9e7e2 60%,#d9c08a 80%,#f2d23c 100%)}
  .brand{position:absolute;left:60px;top:118px;color:var(--white);font-family:"Poppins",sans-serif;font-weight:800;line-height:1}
  .brand .name{display:block;font-size:64px;letter-spacing:1px}
  .brand .tag{display:block;font-size:22px;letter-spacing:1.5px;margin-top:8px;padding-left:120px}
  .blue-panel{position:absolute;left:44px;top:227px;width:406px;height:843px;background:var(--blue)}
  .panel-art{position:absolute;left:0;top:0}
  .services-pill{position:absolute;left:450px;top:350px;width:397px;height:62px;background:var(--lime);border-radius:0 31px 31px 0}
  .services-pill h2{position:absolute;left:17px;top:2px;font-family:"Bebas Neue",sans-serif;font-weight:400;font-size:56px;letter-spacing:6px;color:var(--charcoal);line-height:62px}
  .services-pill .rule{position:absolute;left:328px;top:29px;width:58px;height:5px;background:var(--charcoal);border-radius:3px}
  .services{position:absolute;left:458px;top:0;list-style:none}
  .service{position:absolute;left:0;width:420px;display:flex;align-items:center;gap:12px;color:var(--blue);font-weight:700;font-size:27px;line-height:1.05;white-space:nowrap}
  .service svg{flex:none;width:50px;height:50px;fill:none;stroke:var(--lime);stroke-width:2.6;stroke-linecap:round;stroke-linejoin:round}
  .contact-band{position:absolute;left:0;top:1070px;width:900px;height:130px;background:var(--lime)}
  .discount{position:absolute;left:500px;top:940px;z-index:2;overflow:visible}
  .contact{position:absolute;font-family:"Oswald",sans-serif;font-weight:500;color:var(--charcoal);line-height:1;display:flex;align-items:center;white-space:nowrap}
  .contact svg{flex:none;fill:none;stroke:var(--blue);stroke-width:2.4;stroke-linecap:round;stroke-linejoin:round}
  .contact.phone{left:158px;top:1090px;font-size:34px;gap:16px}
  .contact.email{left:46px;top:1141px;font-size:28px;gap:16px}
  .contact.social{left:514px;top:1100px;font-size:26px;gap:8px}
</style>
</head>
<body>
<main class="flyer">
  <div class="top-band"></div>
  <div class="tools-photo" role="img" aria-label="Photo of plumbing tools: chrome tap, pressure gauge, brass fittings, pliers, spirit level and building plans"></div>

  <div class="brand">
    <span class="name">KESTREL</span>
    <span class="tag">PLUMBING SOLUTIONS</span>
  </div>

  <section class="blue-panel">
    <svg class="panel-art" width="406" height="843" viewBox="0 0 406 843">
      <text transform="translate(118 815) rotate(-90)" font-family="Oswald, sans-serif" font-weight="300" font-size="118" fill="#ffffff" textLength="777" lengthAdjust="spacingAndGlyphs">PLUMBING SOLUTIONS</text>
      <g font-family="'Bebas Neue', sans-serif" fill="#3a3a3c" text-anchor="end">
        <text x="379" y="108" font-size="86" textLength="158" lengthAdjust="spacingAndGlyphs">YOUR</text>
        <rect x="345" y="102" width="46" height="5" fill="#3a3a3c"/>
        <text x="379" y="181" font-size="86" textLength="148" lengthAdjust="spacingAndGlyphs">LOCAL</text>
        <text x="379" y="255" font-size="86" textLength="223" lengthAdjust="spacingAndGlyphs">RELIABLE</text>
        <text x="379" y="326" font-size="86" textLength="203" lengthAdjust="spacingAndGlyphs">SYDNEY</text>
        <text x="379" y="400" font-size="86" textLength="223" lengthAdjust="spacingAndGlyphs">PLUMBER</text>
      </g>
      <rect x="156" y="423" width="260" height="18" rx="9" fill="#ffffff"/>
      <g font-family="Poppins, sans-serif" font-weight="800" fill="#ffffff">
        <text x="156" y="492" font-size="34" textLength="223" lengthAdjust="spacingAndGlyphs">SPECIALISING</text>
        <text x="156" y="522" font-size="24" textLength="223" lengthAdjust="spacingAndGlyphs">IN ALL ASPECTS OF:</text>
      </g>
      <g font-family="'Bebas Neue', sans-serif" fill="#b8ea4c">
        <text x="156" y="610" font-size="92" textLength="223" lengthAdjust="spacingAndGlyphs">PLUMING</text>
        <text x="156" y="695" font-size="88" textLength="223" lengthAdjust="spacingAndGlyphs">DRAINAGE</text>
        <text x="156" y="785" font-size="92" textLength="88" lengthAdjust="spacingAndGlyphs">GAS</text>
        <text x="156" y="815" font-size="38" textLength="155" lengthAdjust="spacingAndGlyphs">MAINTENANCE</text>
      </g>
    </svg>
  </section>

  <div class="services-pill">
    <h2>OUR SERVICES</h2>
    <span class="rule"></span>
  </div>

  <ul class="services">
    <li class="service" style="top:425px"><svg viewBox="0 0 50 50"><circle cx="24" cy="26" r="20"/><text x="24" y="31" text-anchor="middle" font-size="13" font-family="Poppins, sans-serif" font-weight="700" fill="#b8ea4c" stroke="none">24</text><path d="M40 4v10M35 9h10"/></svg>Emergency Plumbing</li>
    <li class="service" style="top:483px"><svg viewBox="0 0 50 50"><path d="M6 12h30a8 8 0 0 1 0 16H14a8 8 0 0 0 0 16h24"/><path d="M32 36l4 4 8-8"/></svg>Plumbing Maintenance</li>
    <li class="service" style="top:541px"><svg viewBox="0 0 50 50"><rect x="4" y="8" width="42" height="10" rx="2"/><path d="M14 18v8M30 22l14 22M26 26l6-4"/><path d="M8 28c0 3 4 3 4 0l-2-4z"/></svg>Drainage Maintenance</li>
    <li class="service" style="top:600px"><svg viewBox="0 0 50 50"><path d="M25 4c8 10 14 16 14 26a14 14 0 0 1-28 0c0-6 3-10 6-13 0 5 3 7 5 7-2-8 1-14 3-20z"/><path d="M25 32c3 3 4 5 4 8a4 4 0 0 1-8 0c0-3 2-5 4-8z" fill="#b8ea4c"/></svg>Gas Maintenance</li>
    <li class="service" style="top:662px"><svg viewBox="0 0 50 50"><rect x="6" y="10" width="26" height="34" rx="3"/><path d="M19 22c3 4 4 6 4 8a4 4 0 0 1-8 0c0-2 1-4 4-8z" fill="#b8ea4c"/><path d="M32 18h8M32 36h8M44 12v32M16 4v4M20 4v4"/></svg>Hot Water Systems</li>
    <li class="service" style="top:720px"><svg viewBox="0 0 50 50"><path d="M4 40V26h22V14h14v10M34 6v8M40 6v6M30 6h14"/><path d="M24 32c3 4 4 6 4 8a4 4 0 0 1-8 0c0-2 1-4 4-8z"/></svg>Leaking Fixtures</li>
    <li class="service" style="top:788px"><svg viewBox="0 0 50 50"><path d="M8 4v34h36M14 4v28h30M8 8h6M32 26v18M38 26v18"/></svg><span>Blocked Sewer &amp;<br>Stormwater</span></li>
    <li class="service" style="top:858px"><svg viewBox="0 0 50 50"><rect x="12" y="16" width="26" height="20" rx="4"/><circle cx="25" cy="26" r="5"/><path d="M20 16l2-4h6l2 4M6 16c-3 6-3 14 0 20M44 16c3 6 3 14 0 20"/></svg>Camera &amp; Locating</li>
    <li class="service" style="top:908px"><svg viewBox="0 0 50 50"><path d="M22 6C12 18 6 26 6 34a14 14 0 0 0 24 9"/><rect x="32" y="6" width="10" height="28" rx="5"/><circle cx="37" cy="38" r="7"/><circle cx="16" cy="32" r="3" fill="#b8ea4c"/><circle cx="22" cy="24" r="2" fill="#b8ea4c"/></svg>TMV Maintenance</li>
  </ul>

  <footer class="contact-band"></footer>

  <svg class="discount" width="330" height="150" viewBox="0 0 330 150">
    <defs>
      <path id="badge-arc" d="M31 175 A131 131 0 0 1 293 175"/>
      <clipPath id="badge-clip"><rect x="0" y="0" width="330" height="130"/></clipPath>
    </defs>
    <circle cx="162" cy="175" r="117" fill="#b8ea4c" clip-path="url(#badge-clip)"/>
    <text font-family="Poppins, sans-serif" font-weight="700" font-size="23" fill="#2f2f31"><textPath href="#badge-arc" startOffset="50%" text-anchor="middle" textLength="340" lengthAdjust="spacingAndGlyphs">MENTION THIS FLYER TO RECEIVE</textPath></text>
    <text x="162" y="102" text-anchor="middle" font-family="Poppins, sans-serif" font-weight="800" font-size="58" fill="#3a3a3c">15%</text>
    <text x="162" y="131" text-anchor="middle" font-family="Poppins, sans-serif" font-weight="800" font-size="31" fill="#3a3a3c" textLength="195" lengthAdjust="spacingAndGlyphs">DISCOUNT!</text>
  </svg>

  <div class="contact phone"><svg width="38" height="38" viewBox="0 0 38 38"><path d="M8 3l7 7-4 5c2 5 6 9 11 11l5-4 7 7-5 6C16 34 4 22 3 8z"/></svg>0400 555 219</div>
  <div class="contact email"><svg width="40" height="30" viewBox="0 0 40 30"><rect x="2" y="2" width="36" height="26"/><path d="M2 2l18 15L38 2M2 28l13-13M38 28L25 15"/></svg>kestrelplumbingsolutions@mail.com</div>
  <div class="contact social"><svg width="40" height="72" viewBox="0 0 40 76"><rect x="2" y="2" width="36" height="72" rx="6"/><path d="M14 6h12"/><rect x="10" y="18" width="20" height="18" rx="3"/><rect x="10" y="44" width="20" height="18" rx="3"/></svg>@KestrelPlumbingSolutions</div>
</main>
</body>
</html>
```